Muay Thai gym needs an KICK-A$$ NEW timetablefor classes

Dak Ro is Canberra's home of authentic Muay Thai, and we need a new timetable for our ever expanding list of classes!<br/><br/>A document containing all classes & information is included, as well as our logo in .png and .eps formats.

Font styles to use
Serif
Sans Serif

Colors

Designer to choose colors to be used in the design.

```html
<!DOCTYPE html>
<html lang="en">
<head>
<meta charset="utf-8">
<title>Dak Ro — 2020 Class Timetable</title>
<link href="https://fonts.googleapis.com/css2?family=Arimo:wght@400;700&family=Archivo+Black&display=swap" rel="stylesheet">
<style>
  :root{
    --green:#076839;
    --blue:#00aeef;
    --sage:#c8d0c2;
    --sky:#c5e8f8;
    --cream:#fcf8c6;
    --grey:#d6d6d6;
    --ink:#111;
    --white:#fff;
    --row:16.46px;
  }
  *{box-sizing:border-box;margin:0;padding:0}
  html,body{width:1200px;height:848px;overflow:hidden;background:var(--white)}
  body{position:relative;font-family:"Arimo",Arial,sans-serif}

  /* left brand panel */
  .brand{position:absolute;left:10px;top:16px;width:144px;height:115px;display:flex;flex-direction:column;align-items:center;justify-content:center;gap:8px}
  .brand-mark{width:30px;height:30px;background:var(--green)}
  .brand-name{font-family:"Archivo Black",Arial,sans-serif;font-size:30px;color:var(--green);letter-spacing:1px}
  .year-banner{position:absolute;left:12px;top:155px;width:138px;height:85px;border-radius:10px 40px 10px 40px;background:linear-gradient(160deg,#0b7a45,var(--green))}
  .address{position:absolute;left:6px;top:272px;width:148px;text-align:center;color:var(--green);font-weight:700;font-size:21px;line-height:25.6px}

  .social{position:absolute;left:16px;top:499px;width:126px;height:338px;background:var(--green)}
  .social-icons{position:absolute;top:5px;left:6px;right:6px;display:flex;justify-content:space-between}
  .social-icons span{width:31px;height:27px;background:var(--white)}
  .social-links{position:absolute;top:40px;left:0;width:126px;height:290px}
  .social-links p{position:absolute;top:0;color:var(--white);font-size:19px;writing-mode:vertical-rl;white-space:nowrap}

  /* timetable */
  .timetable{position:absolute;left:159px;top:9px;display:grid;
    grid-template-columns:63px 31px 72px 71px 72px 75px 73px 71px 72px 71px 77px 71px 72px 72px 71px;
    grid-template-rows:41px repeat(48,var(--row));
    outline:1.5px solid var(--ink)}
  .head{display:flex;align-items:center;justify-content:center;font-weight:700;font-size:17px;background:var(--cream);border-left:1px solid var(--ink);border-bottom:1px solid var(--ink)}
  .head.time{background:var(--grey);color:var(--ink);font-size:14px;border-left:0}
  .head.green{color:var(--green)} .head.blue{color:var(--blue)}

  .hours{grid-column:1;grid-row:2/50;display:flex;flex-direction:column}
  .hours div{height:calc(var(--row)*4);display:flex;align-items:center;justify-content:center;gap:5px;border-bottom:1px solid var(--ink);font-weight:700;font-size:21px}
  .hours small{font-size:16px}
  .minutes{grid-column:2;grid-row:2/50;display:flex;flex-direction:column;border-left:1px solid var(--ink)}
  .minutes span{height:var(--row);display:flex;align-items:center;justify-content:center;font-size:11px;border-bottom:1px solid #bbb;background:var(--white)}
  .minutes span:nth-child(4n){border-bottom-color:var(--ink)}

  .day{grid-row:2/50;border-left:1px solid var(--ink);
    background-image:repeating-linear-gradient(to bottom,transparent 0 calc(var(--row) - 1px),var(--white) calc(var(--row) - 1px) var(--row))}
  .day.sage{background-color:var(--sage)}
  .day.sky{background-color:var(--sky)}
  .hour-lines{grid-column:3/16;grid-row:2/50;pointer-events:none;
    background-image:repeating-linear-gradient(to bottom,transparent 0 calc(var(--row)*4 - 1px),var(--ink) calc(var(--row)*4 - 1px) calc(var(--row)*4))}

  .class{display:flex;align-items:center;justify-content:center;text-align:center;color:var(--white);font-size:11.5px;line-height:14px;padding:0 2px;box-shadow:inset 0 0 0 .5px rgba(255,255,255,.85)}
  .class.g{background:var(--green)}
  .class.b{background:var(--blue)}
  .sunday{grid-column:15;grid-row:2/50;background:var(--green);display:flex;align-items:center;justify-content:center;border-left:1px solid var(--ink)}
  .sunday p{transform:rotate(-90deg);white-space:nowrap;color:var(--white);font-weight:700;font-size:20px}
</style>
</head>
<body>

<div class="brand">
  <span class="brand-mark"></span>
  <span class="brand-name">DAK RO</span>
</div>
<div class="year-banner" role="img" aria-label="Ribbon banner with the season year 2020"></div>
<p class="address">Level 1,<br>52<br>Kembla Road,<br>Fyshwick,<br>Canberra</p>

<div class="social">
  <div class="social-icons"><span></span><span></span><span></span></div>
  <div class="social-links">
    <p style="left:18px">dakrocanberra.com/news</p>
    <p style="left:55px">dakrocanberra.com/team</p>
    <p style="left:92px">dakrocanberra.com/gallery</p>
  </div>
</div>

<div class="timetable">
  <div class="head time" style="grid-column:1/3">TIME</div>
  <div class="head green" style="grid-column:3/5">Monday</div>
  <div class="head blue" style="grid-column:5/8">Tuesday</div>
  <div class="head green" style="grid-column:8/10">Wednesday</div>
  <div class="head blue" style="grid-column:10/13">Thursday</div>
  <div class="head green" style="grid-column:13/14">Friday</div>
  <div class="head blue" style="grid-column:14/15">Saturday</div>
  <div class="head green" style="grid-column:15/16">Sunday</div>

  <div class="hours">
    <div>6 <small>AM</small></div><div>7 <small>AM</small></div><div>8 <small>AM</small></div><div>9 <small>AM</small></div>
    <div>10 <small>AM</small></div><div>11 <small>AM</small></div><div>12 <small>PM</small></div><div>1 <small>PM</small></div>
    <div>4 <small>AM</small></div><div>5 <small>AM</small></div><div>6 <small>AM</small></div><div>7 <small>AM</small></div>
  </div>
  <div class="minutes">
    <span>00</span><span>15</span><span>30</span><span>45</span><span>00</span><span>15</span><span>30</span><span>45</span>
    <span>00</span><span>15</span><span>30</span><span>45</span><span>00</span><span>15</span><span>30</span><span>45</span>
    <span>00</span><span>15</span><span>30</span><span>45</span><span>00</span><span>15</span><span>30</span><span>45</span>
    <span>00</span><span>15</span><span>30</span><span>45</span><span>00</span><span>15</span><span>30</span><span>45</span>
    <span>00</span><span>15</span><span>30</span><span>45</span><span>00</span><span>15</span><span>30</span><span>45</span>
    <span>00</span><span>15</span><span>30</span><span>45</span><span>00</span><span>15</span><span>30</span><span>45</span>
  </div>

  <div class="day sage" style="grid-column:3/5"></div>
  <div class="day sky" style="grid-column:5/8"></div>
  <div class="day sage" style="grid-column:8/10"></div>
  <div class="day sky" style="grid-column:10/13"></div>
  <div class="day sage" style="grid-column:13/14"></div>
  <div class="day sky" style="grid-column:14/15"></div>
  <div class="hour-lines"></div>

  <!-- Monday -->
  <div class="class g" style="grid-column:3/5;grid-row:2/5">Muay Thai<br>(All Experience)</div>
  <div class="class g" style="grid-column:3/5;grid-row:36/39">Junior &amp; Teenage<br>Muay Thai</div>
  <div class="class g" style="grid-column:3/4;grid-row:40/44">Muay Thai<br>(All<br>Experience)</div>
  <div class="class g" style="grid-column:4/5;grid-row:40/44">Muay Thai<br>for<br>Beginners</div>
  <div class="class g" style="grid-column:3/5;grid-row:44/48">Padwork</div>
  <div class="class g" style="grid-column:3/5;grid-row:48/50">Sparring<br>(Must do Padwork)</div>

  <!-- Tuesday -->
  <div class="class b" style="grid-column:5/8;grid-row:2/5">Fighters</div>
  <div class="class b" style="grid-column:5/8;grid-row:30/33">Muay Thai (All Experience)</div>
  <div class="class b" style="grid-column:5/8;grid-row:36/39">Junior &amp; Teenage<br>Muay Thai</div>
  <div class="class b" style="grid-column:5/6;grid-row:40/44">Padwork</div>
  <div class="class b" style="grid-column:6/7;grid-row:42/48">Muay Thai (Development/ Intermediate &amp; Fighters)</div>
  <div class="class b" style="grid-column:7/8;grid-row:44/48">Muay Thai</div>

  <!-- Wednesday -->
  <div class="class g" style="grid-column:8/10;grid-row:2/5">Muay Thai<br>(All Experience)</div>
  <div class="class g" style="grid-column:8/9;grid-row:40/44">Muay Thai<br>(All Levels)</div>
  <div class="class g" style="grid-column:9/10;grid-row:40/44">Muay Thai<br>for<br>Beginners</div>
  <div class="class g" style="grid-column:8/10;grid-row:44/48">Padwork</div>
  <div class="class g" style="grid-column:8/10;grid-row:48/50">Sparring (Must do<br>Padwork)</div>

  <!-- Thursday -->
  <div class="class b" style="grid-column:10/13;grid-row:2/6">Fighters</div>
  <div class="class b" style="grid-column:10/13;grid-row:30/33">Muay Thai (All Experience)</div>
  <div class="class b" style="grid-column:10/13;grid-row:36/39">Junior &amp; Teenage Muay Thai</div>
  <div class="class b" style="grid-column:10/11;grid-row:40/44">Padwork</div>
  <div class="class b" style="grid-column:11/12;grid-row:42/48">Muay Thai (Development/ Intermediate &amp; Fighters)</div>
  <div class="class b" style="grid-column:12/13;grid-row:44/48">Beginners Sparring &amp; Clinching</div>

  <!-- Friday -->
  <div class="class g" style="grid-column:13/14;grid-row:2/5">Muay Thai<br>(All<br>Experience)</div>
  <div class="class g" style="grid-column:13/14;grid-row:36/44">Thai Style</div>

  <!-- Saturday -->
  <div class="class b" style="grid-column:14/15;grid-row:10/13">Muay Thai</div>
  <div class="class b" style="grid-column:14/15;grid-row:14/20">Fighters</div>
  <div class="class b" style="grid-column:14/15;grid-row:22/25">Junior &amp;<br>Teenage<br>Muay Thai</div>
  <div class="class b" style="grid-column:14/15;grid-row:26/30">Muay<br>Thai (All<br>Experience)</div>

  <!-- Sunday -->
  <div class="sunday"><p>Personal training available seven days a week, including Sunday!</p></div>
</div>

</body>
</html>
```